Business Card for Makeup Artist

I need a business card designed for my makeup and hair artistry business which is primarily events and weddings focused. The card needs to be sleek, simple, stylish and appealing to women. I would prefer a white background but open to suggestions also. I also love the marble background look. I have attached some example pics. It needs to be a double sided card with logo and/or design on one side and contact details in the centre of the card on the other side. NO LOGO ON BACK. Examples attached.

Target Market(s)

Females age 14-55

Industry/Entity Type

Business

Contact Information for Business Card

Nora Vint
Principal Makeup Artist
P: 0413 925 214
E: nora@lumirabeauty.com.au
W: www.lumirabeauty.com.au

Requirements
Should not have
• No yellow, green, red or blue in the design.

```html
<!DOCTYPE html>
<html lang="en">
<head>
<meta charset="utf-8">
<title>Lumira Makeup Artistry – Business Card</title>
<link rel="stylesheet" href="https://fonts.googleapis.com/css2?family=Raleway:wght@400;500&display=swap">
<style>
  :root {
    --backdrop: #eceef0;
    --marble-dark: #141414;
    --marble-mid: #343434;
    --card-white: #f4f4f3;
    --frame-line: #1a1a1a;
    --ink: #1c1c1c;
    --ink-soft: #3a3a3a;
    --logo-grey: #555555;
    --accent-pink: #d94aa0;
  }
  * { box-sizing: border-box; margin: 0; padding: 0; }
  html, body { width: 1200px; height: 800px; overflow: hidden; }
  body {
    background: var(--backdrop);
    font-family: "Raleway", Arial, sans-serif;
    position: relative;
  }
  .card {
    position: absolute;
    top: 257px;
    width: 500px;
    height: 286px;
    box-shadow: 0 6px 18px rgba(0,0,0,0.12);
    overflow: hidden;
  }
  .card--front { left: 70px; }
  .card--back { left: 630px; }

  .marble {
    position: absolute;
    inset: 0;
    background: radial-gradient(ellipse at 35% 40%, var(--marble-mid), var(--marble-dark) 75%);
  }

  /* Front side */
  .logo-panel {
    position: absolute;
    left: 62px; right: 62px; top: 46px; bottom: 46px;
    background: var(--card-white);
    padding: 8px;
  }
  .logo-panel__frame {
    width: 100%; height: 100%;
    border: 2px solid var(--frame-line);
    display: flex;
    align-items: center;
    justify-content: center;
    gap: 10px;
  }
  .logo-dot {
    flex: 0 0 auto;
    width: 10px; height: 10px;
    border-radius: 50%;
    background: var(--accent-pink);
  }
  .logo-name {
    font-weight: 500;
    font-size: 19px;
    letter-spacing: 1px;
    color: var(--logo-grey);
    text-transform: uppercase;
    white-space: nowrap;
  }

  /* Back side */
  .details-panel {
    position: absolute;
    inset: 24px;
    background: var(--card-white);
    padding: 5px;
  }
  .details-panel__frame {
    width: 100%; height: 100%;
    border: 2px solid var(--frame-line);
    padding: 4px;
  }
  .details-panel__inner {
    width: 100%; height: 100%;
    border: 1px solid var(--frame-line);
    padding: 52px 0 0 54px;
  }
  .contact-name {
    font-size: 27px;
    font-weight: 500;
    color: var(--ink);
    line-height: 1.1;
  }
  .contact-role {
    font-size: 21px;
    font-weight: 400;
    color: var(--ink-soft);
    margin-top: 2px;
  }
  .contact-list {
    list-style: none;
    margin-top: 34px;
    font-size: 12px;
    color: var(--ink-soft);
    line-height: 1.45;
  }
</style>
</head>
<body>
  <section class="card card--front" aria-label="Card front">
    <div class="marble" role="img" aria-label="Black and white marble texture"></div>
    <div class="logo-panel">
      <div class="logo-panel__frame">
        <span class="logo-dot"></span>
        <span class="logo-name">Lumira Makeup Artistry</span>
      </div>
    </div>
  </section>

  <section class="card card--back" aria-label="Card back">
    <div class="marble" role="img" aria-label="Black and white marble texture"></div>
    <div class="details-panel">
      <div class="details-panel__frame">
        <div class="details-panel__inner">
          <h1 class="contact-name">Nora Vint</h1>
          <p class="contact-role">Principal Makeup Artist</p>
          <ul class="contact-list">
            <li>P: 0413 925 214</li>
            <li>E: nora@lumirabeauty.com.au</li>
            <li>W: www.lumirabeauty.com.au</li>
          </ul>
        </div>
      </div>
    </div>
  </section>
</body>
</html>
```